Web Design Project

We are telecom company based in the Netherlands and we want to create a new design for our company website.

It needs to give a professional, easy to use and clean look.

We currently have an old website. http://www.dial-brook.com we have started setting up a new site with all the new textual content. We are currently looking for the new look, you can have an idea what we are looking for at the new website location at http://www.dial-brook.com/nl where the new site is being setup.

We deliver telephone systems and infrastructure like INTERNET and telephone lines. We want to focus on government and cooperate companies.

The logo has the red color that is why we want to use red in the new design.

Target Market(s)

goverment and companies

Industry/Entity Type

Government

```html
<!DOCTYPE html>
<html lang="nl">
<head>
<meta charset="utf-8">
<title>Dial Brook – Telefonie voor overheid en bedrijven</title>
<link href="https://fonts.googleapis.com/css2?family=Ubuntu:wght@400;500;700&family=Arimo:wght@400;700&display=swap" rel="stylesheet">
<style>
:root{
  --red:#e8141c;
  --red-dark:#c40d14;
  --brown:#463f3b;
  --brown-line:#5a524d;
  --page:#ededeb;
  --panel:#f4f4f2;
  --panel-edge:#e0e0dc;
  --ink:#333;
  --muted:#555;
  --white:#fff;
}
*{margin:0;padding:0;box-sizing:border-box}
html,body{width:993px;height:1200px;overflow:hidden}
body{position:relative;background:var(--page);font-family:"Arimo",Arial,sans-serif;color:var(--ink)}
.abs{position:absolute}
.header-band{left:0;top:0;width:993px;height:158px;background:var(--brown)}
.brand{left:91px;top:10px;display:flex;align-items:center;gap:8px}
.brand-dot{width:106px;height:106px;border-radius:50%;background:var(--red)}
.brand-name{font-family:"Ubuntu",sans-serif;font-weight:500;font-size:22px;color:var(--white)}
.search{left:731px;top:27px;width:167px;height:22px;border-radius:11px;background:var(--white);border:2px solid #d8d8d8;font-family:"Ubuntu",sans-serif;font-size:11px;color:#555;padding:3px 0 0 16px}
.search svg{position:absolute;right:10px;top:3px}
.nav{left:391px;top:73px;height:30px;font-family:"Ubuntu",sans-serif;font-size:12px;color:var(--white)}
.nav a{position:absolute;top:7px;white-space:nowrap;color:var(--white);text-decoration:none}
.nav .active{left:0;top:0;width:68px;height:30px;background:var(--red);border:1px solid #fff;text-align:center;line-height:28px}
.panel{background:var(--panel);border:1px solid var(--panel-edge);border-radius:10px;box-shadow:0 0 3px rgba(0,0,0,.06)}
.hero{left:80px;top:126px;width:832px;height:295px}
.img-fill{background:linear-gradient(135deg,#d9d9db,#6a6a70 60%,#2b2b30)}
.hero-phones{left:19px;top:34px;width:324px;height:246px;border-radius:6px}
.hero-title{left:361px;top:27px;font-family:"Ubuntu",sans-serif;font-weight:700;font-size:31px;color:#333}
.hero-title .red{color:var(--red)}
.hero-text{left:365px;top:80px;width:450px;font-size:10.4px;line-height:15.5px;text-align:justify;letter-spacing:.2px}
.hero-text p+p{margin-top:15.5px}
.hero-text b{color:#111}
.btn-read{left:366px;top:216px;width:115px;height:33px;border-radius:9px;background:var(--red);border:2px solid #fff;box-shadow:0 0 0 1px var(--red);color:#fff;font-family:"Ubuntu",sans-serif;font-size:15px;text-align:center;line-height:29px}
.hero-deco{left:697px;top:181px;width:126px;height:107px;border-radius:50%;background:radial-gradient(circle,#e8141c 0,#e8141c 30%,rgba(232,20,28,.25) 31%,rgba(232,20,28,0) 70%)}
.card{top:436px;width:248px;height:257px}
.card h2{position:absolute;left:20px;top:17px;font-family:"Ubuntu",sans-serif;font-weight:700;font-size:15.5px;color:var(--red);white-space:nowrap}
.num{position:absolute;left:19px;top:52px;width:25px;height:25px;border-radius:50%;background:var(--red);color:#fff;font-family:"Ubuntu",sans-serif;font-weight:700;font-size:15px;text-align:center;line-height:25px}
.sub{position:absolute;left:51px;top:53px;font-family:"Ubuntu",sans-serif;font-size:10.5px;line-height:14px;white-space:nowrap}
.sub b{color:var(--red);font-weight:500}
.sub span{color:#333;font-weight:500}
.list{position:absolute;left:20px;top:100px;list-style:none;font-size:10px;letter-spacing:.4px;color:#444}
.list li{height:20.7px;display:flex;align-items:center;gap:9px;white-space:nowrap}
.card-body{position:absolute;left:20px;top:100px;width:210px;font-size:10px;line-height:20.7px;letter-spacing:.35px;color:#444;text-align:justify}
.more{font-family:"Ubuntu",sans-serif;font-weight:500;font-size:10.5px;color:var(--red)}
.welcome{left:80px;top:712px;width:549px;height:259px}
.welcome h2{position:absolute;left:18px;top:27px;font-family:"Ubuntu",sans-serif;font-weight:700;font-size:21px;color:#333}
.welcome h2 .red{color:var(--red)}
.welcome-text{position:absolute;left:18px;top:69px;width:310px;font-size:9.8px;line-height:17.3px;letter-spacing:.2px;color:#444;text-align:justify}
.welcome-text p+p{margin-top:9px}
.checks{position:absolute;left:22px;top:205px;list-style:none;font-family:"Ubuntu",sans-serif;font-size:11.5px;color:#333}
.checks li{height:20.7px;display:flex;align-items:center;gap:10px}
.agent{left:334px;top:5px;width:208px;height:249px;border-radius:0 0 10px 0;background:linear-gradient(180deg,#e9ddd2,#c9a68e 55%,#f0ece8)}
.contact{left:665px;top:712px;width:247px;height:259px}
.contact h2{position:absolute;left:13px;top:17px;font-family:"Ubuntu",sans-serif;font-weight:700;font-size:15.5px;color:var(--red)}
.desk-phone{left:121px;top:46px;width:120px;height:78px;border-radius:8px;background:linear-gradient(135deg,#8a8f96,#2f3338)}
.c-label{position:absolute;font-family:"Ubuntu",sans-serif;font-weight:500;font-size:10.5px;color:var(--red)}
.c-text{position:absolute;font-size:9.8px;line-height:20.7px;letter-spacing:.3px;color:#444;white-space:nowrap}
.footer{left:0;top:1004px;width:993px;height:196px;background:var(--brown);color:#fff;font-family:"Ubuntu",sans-serif}
.fcol{position:absolute;top:18px}
.fcol h3{font-weight:700;font-size:13px;margin-bottom:14px}
.fcol ul{list-style:none;font-size:10.5px}
.fcol li{height:20.7px;display:flex;align-items:center;gap:10px;white-space:nowrap}
.fcol li::before{content:"";border-left:4px solid #fff;border-top:3px solid transparent;border-bottom:3px solid transparent}
.fdiv{position:absolute;top:32px;width:1px;height:121px;background:var(--brown-line)}
.fbottom{position:absolute;left:89px;top:172px;font-size:11.5px;word-spacing:2px}
.fcopy{position:absolute;left:635px;top:172px;font-size:11.5px}
</style>
</head>
<body>

<div class="abs header-band"></div>
<div class="abs brand"><div class="brand-dot"></div><span class="brand-name">Dial Brook</span></div>
<div class="abs search">------ Search here ----
  <svg width="18" height="14" viewBox="0 0 18 14"><circle cx="6" cy="7" r="5.5" fill="none" stroke="#555"/><path d="M1 7h10M6 1.5v11M2.5 4h7M2.5 10h7" stroke="#555" stroke-width=".7"/><line x1="11" y1="9" x2="17" y2="13" stroke="#333" stroke-width="2"/></svg>
</div>
<nav class="abs nav" style="width:520px">
  <a class="active" href="#">Home</a>
  <a style="left:84px" href="#">Dial-Brook</a>
  <a style="left:164px" href="#">Producten</a>
  <a style="left:248px" href="#">Diensten</a>
  <a style="left:324px" href="#">Reseller</a>
  <a style="left:394px" href="#">Support</a>
  <a style="left:466px" href="#">Contact</a>
</nav>

<section class="abs panel hero">
  <div class="abs img-fill hero-phones" role="img" aria-label="Drie smartphones met toetsenbord en touchscreen"></div>
  <h1 class="abs hero-title"><span class="red">Dial</span> Brook</h1>
  <div class="abs hero-text">
    <p><b>Welkom bij Dial-Brook! U wilt efficiënter werken, beter bereikbaar zijn en kosten besparen?De telefooncentrales van Dial-Brook</b> helpen u hierbij. Dial-Brook biedt telefooncentrales aan waarin alle denkbare oplossingen zijn geïntegreerd.</p>
    <p>De centrales zijn zelfs zo compleet dat achteraf uitbreiden tot het verleden behoort.U krijgt een kant-en-klare oplossing waarmee u niet alleen vandaag, maar ook morgen op een efficiënte, betrouwbare en professionele manier uw telefonie</p>
  </div>
  <div class="abs btn-read">Read more</div>
  <div class="abs hero-deco" role="img" aria-label="Rode illustratie met telefoon, kaart, gebouwen en scherm rond een centrale wolk"></div>
</section>

<section class="abs panel card" style="left:80px">
  <h2>Daarom Velmar Telecom!</h2>
  <div class="num">1</div>
  <div class="sub"><b>Lorem ipsum dolor sit</b><br><span>amet,consectetuadipisicing elit</span></div>
  <ul class="list">
    <li><svg width="17" height="10"><path d="M0 5h14M9 1l5 4-5 4" stroke="#e8141c" stroke-width="2" fill="none"/></svg>Altijd de meest voordelige tarieven</li>
    <li><svg width="17" height="10"><path d="M0 5h14M9 1l5 4-5 4" stroke="#e8141c" stroke-width="2" fill="none"/></svg>Zowel nationaal als internationaal</li>
    <li><svg width="17" height="10"><path d="M0 5h14M9 1l5 4-5 4" stroke="#e8141c" stroke-width="2" fill="none"/></svg>Zowel voor vast als mobiel</li>
    <li><svg width="17" height="10"><path d="M0 5h14M9 1l5 4-5 4" stroke="#e8141c" stroke-width="2" fill="none"/></svg>Vanaf elke telefoon in de wereld</li>
    <li><svg width="17" height="10"><path d="M0 5h14M9 1l5 4-5 4" stroke="#e8141c" stroke-width="2" fill="none"/></svg>Gratis aansluiting en/of activatie</li>
    <li><svg width="17" height="10"><path d="M0 5h14M9 1l5 4-5 4" stroke="#e8141c" stroke-width="2" fill="none"/></svg>Geen onnodige abonnementskosten</li>
    <li><svg width="17" height="10"><path d="M0 5h14M9 1l5 4-5 4" stroke="#e8141c" stroke-width="2" fill="none"/></svg>Transparantie en heldere inzage</li>
  </ul>
</section>

<section class="abs panel card" style="left:375px;width:247px">
  <h2 style="left:25px">Onze Diensten</h2>
  <div class="num" style="left:21px">2</div>
  <div class="sub" style="left:53px"><b>Lorem ipsum dolor sit</b><br><span>amet,consectetuadipisicing elit</span></div>
  <div class="card-body">Lorem Ipsum is simply dummy text of the printing and typesetting industry. Lorem Ipsum has been the industry's standard dummy text ever since the 1500s, when an unknown printer took a galley of type and scrambled it ries, unchanged
    <div class="more" style="margin-top:2px;margin-left:3px">View more [+]</div>
  </div>
</section>

<section class="abs panel card" style="left:663px">
  <h2 style="left:20px">De meest voordelige beltar</h2>
  <div class="num" style="left:20px">3</div>
  <div class="sub" style="left:52px"><b>Lorem ipsum dolor sit</b><br><span>amet,consectetuadipisicing elit</span></div>
  <ul class="list" style="left:24px">
    <li><svg width="13" height="11"><rect x=".5" y="2.5" width="9" height="8" fill="none" stroke="#e8141c"/><path d="M2 6l3 3 7-8" stroke="#e8141c" stroke-width="2" fill="none"/></svg>Altijd de meest voordelige tarieven</li>
    <li><svg width="13" height="11"><rect x=".5" y="2.5" width="9" height="8" fill="none" stroke="#e8141c"/><path d="M2 6l3 3 7-8" stroke="#e8141c" stroke-width="2" fill="none"/></svg>Zowel nationaal als internationaal</li>
    <li><svg width="13" height="11"><rect x=".5" y="2.5" width="9" height="8" fill="none" stroke="#e8141c"/><path d="M2 6l3 3 7-8" stroke="#e8141c" stroke-width="2" fill="none"/></svg>Zowel voor vast als mobiel</li>
    <li><svg width="13" height="11"><rect x=".5" y="2.5" width="9" height="8" fill="none" stroke="#e8141c"/><path d="M2 6l3 3 7-8" stroke="#e8141c" stroke-width="2" fill="none"/></svg>Vanaf elke telefoon in de wereld</li>
    <li><svg width="13" height="11"><rect x=".5" y="2.5" width="9" height="8" fill="none" stroke="#e8141c"/><path d="M2 6l3 3 7-8" stroke="#e8141c" stroke-width="2" fill="none"/></svg>Gratis aansluiting en/of activatie</li>
    <li><svg width="13" height="11"><rect x=".5" y="2.5" width="9" height="8" fill="none" stroke="#e8141c"/><path d="M2 6l3 3 7-8" stroke="#e8141c" stroke-width="2" fill="none"/></svg>Geen onnodige abonnementskosten</li>
    <li><svg width="13" height="11"><rect x=".5" y="2.5" width="9" height="8" fill="none" stroke="#e8141c"/><path d="M2 6l3 3 7-8" stroke="#e8141c" stroke-width="2" fill="none"/></svg>Transparantie en heldere inzage</li>
  </ul>
</section>

<section class="abs panel welcome">
  <div class="abs agent" role="img" aria-label="Klantenservicemedewerker met headset"></div>
  <h2><span class="red">Welcome</span> Guest !</h2>
  <div class="welcome-text">
    <p>Dial-Brook biedt complete telecomoplossingen aan met betrouwbare technologie en tal van functionaliteiten die tot nu toe alleen maar waren te krijgen in dure maatwerk oplossingen. Alle gangbare functionaliteiten</p>
    <p>De centrales zijn zeer eenvoudig te installeren. Door middel van gratis meegeleverde software</p>
  </div>
  <div class="more abs" style="left:254px;top:199px">View more [+]</div>
  <ul class="checks">
    <li><svg width="12" height="12"><rect width="12" height="12" fill="#e8141c"/><path d="M2.5 6l2.5 2.5 4.5-5" stroke="#fff" stroke-width="1.6" fill="none"/></svg>Telefooncentrales</li>
    <li><svg width="12" height="12"><rect width="12" height="12" fill="#e8141c"/><path d="M2.5 6l2.5 2.5 4.5-5" stroke="#fff" stroke-width="1.6" fill="none"/></svg>Accessories</li>
  </ul>
</section>

<section class="abs panel contact">
  <h2>Contactgegevens !</h2>
  <div class="abs desk-phone" role="img" aria-label="Zakelijke bureautelefoon"></div>
  <div class="c-label" style="left:15px;top:65px;font-size:12px">Dial-Brook</div>
  <div class="c-text" style="left:15px;top:84px">Lindengracht 48<br>1015 KJ Amsterdam<br>The Netherlands</div>
  <div class="c-label" style="left:17px;top:150px">Telefoon nr. :</div>
  <div class="c-label" style="left:139px;top:150px">Fax nr. :</div>
  <div class="c-text" style="left:17px;top:165px">+31 (0) 20 5 550 142</div>
  <div class="c-text" style="left:139px;top:165px">+31 (0) 20 5 550 143</div>
  <div class="c-label" style="left:21px;top:206px">Email :</div>
  <div class="c-text" style="left:21px;top:222px">info@dial-brook.com</div>
  <div class="more abs" style="left:166px;top:228px">View more [+]</div>
</section>

<footer class="abs footer">
  <div class="fcol" style="left:88px"><h3>Prive telefonie</h3><ul><li>Carrier PreSelect</li><li>Mobile SIMCard</li><li>VoIP</li><li>Worldwide Prepaid</li><li>Easy Access</li></ul></div>
  <div class="fdiv" style="left:255px"></div>
  <div class="fcol" style="left:320px"><h3>Zakelijke telefonie</h3><ul><li>Carrier PreSelect</li><li>Mobile SIMCard</li><li>VoIP</li><li>Worldwide Prepaid</li><li>Easy Access</li></ul></div>
  <div class="fdiv" style="left:515px"></div>
  <div class="fcol" style="left:579px"><h3>Wholesale</h3><ul><li>Carrier PreSelect</li><li>Mobile SIMCard</li><li>VoIP</li><li>Worldwide Prepaid</li><li>Easy Access</li></ul></div>
  <div class="fdiv" style="left:727px"></div>
  <div class="fcol" style="left:784px"><h3>Over dial brook</h3><ul><li>Carrier PreSelect</li><li>Mobile SIMCard</li><li>VoIP</li><li>Worldwide Prepaid</li><li>Easy Access</li></ul></div>
  <div class="fbottom">Home &nbsp;~&nbsp; Dial-Brook &nbsp;~&nbsp; Producten &nbsp;~&nbsp; Diensten &nbsp;~&nbsp; Reseller &nbsp;~&nbsp; Support &nbsp;~&nbsp; Contact</div>
  <div class="fcopy">2012 Kesterveld Telecom BV. Alle rechten voorbehouden</div>
</footer>

</body>
</html>
```